Letterhead

We are looking for a basic letterhead. It should include our logo, website - northpeakkitchenware.com, phone 907.418.3952, toll free 855.392.6180, and fax 907.418.5263, along with our address 4837 Birchwood Lane, Anchorage, AK 99517. I want something that will look good printed in color or black and white.

```html
<!DOCTYPE html>
<html lang="en">
<head>
<meta charset="utf-8">
<title>North Peak Kitchenware — Letterhead</title>
<link rel="stylesheet" href="https://fonts.googleapis.com/css2?family=Montserrat:wght@700&family=Open+Sans:wght@400&family=Cinzel:wght@400;600&display=swap">
<style>
  :root {
    --backdrop: #e6e7e9;
    --paper: #ffffff;
    --navy: #1f4596;
    --navy-light: #2f62b2;
    --brand-red: #c63a4b;
    --ink: #3b3b3b;
    --ink-soft: #555;
    --signature-ink: #6a5aa8;
    --stamp: #9cc8c4;
  }
  * { box-sizing: border-box; margin: 0; padding: 0; }
  html, body {
    width: 1200px; height: 1200px; overflow: hidden;
    background: var(--backdrop);
  }
  .letterhead {
    position: absolute; left: 210px; top: 48px;
    width: 780px; height: 1103px;
    background: var(--paper);
    box-shadow: 0 2px 10px rgba(0,0,0,0.12);
    font-family: "Open Sans", Arial, sans-serif;
    color: var(--ink);
  }
  .brand-name {
    position: absolute; top: 66px; left: 0; width: 100%;
    text-align: center;
    font-family: "Montserrat", Arial, sans-serif;
    font-weight: 700; font-size: 30px; letter-spacing: 1px;
    color: var(--navy);
    text-transform: uppercase;
  }
  .letter {
    position: absolute; top: 258px; left: 83px; right: 60px;
    font-size: 12px; line-height: 17px;
  }
  .recipient { margin-bottom: 17px; }
  .greeting { margin-bottom: 10px; }
  .letter p.body-text { margin-bottom: 17px; text-align: justify; }
  .sign-off { margin-bottom: 22px; }
  .signature-row { display: flex; align-items: center; gap: 10px; }
  .signature-mark {
    width: 80px; height: 46px;
    background: linear-gradient(90deg, rgba(106,90,168,0.25), rgba(106,90,168,0.55), rgba(106,90,168,0.2));
    border-radius: 4px;
  }
  .seal-badge {
    width: 56px; height: 56px; border-radius: 50%;
    border: 3px solid var(--stamp); opacity: 0.7;
  }
  .footer-band {
    position: absolute; left: 0; bottom: 0; width: 780px; height: 80px;
  }
  .band-shape { position: absolute; left: 0; top: 0; width: 780px; height: 80px; }
  .contact-list {
    position: absolute; left: 26px; top: 20px;
    list-style: none; color: #fff;
    font-family: "Cinzel", Georgia, serif;
    font-size: 11px; line-height: 18px; letter-spacing: 0.3px;
  }
  .contact-list li { display: flex; align-items: center; gap: 8px; }
  .contact-icon { flex: 0 0 11px; width: 11px; height: 11px; fill: #fff; }
  .address {
    position: absolute; left: 300px; top: 28px;
    font-family: "Cinzel", Georgia, serif; font-size: 11.5px; line-height: 16px;
    color: #fff; letter-spacing: 0.5px;
  }
  .website {
    position: absolute; right: 22px; top: 6px;
    font-family: "Cinzel", Georgia, serif; font-weight: 600; font-size: 12px;
    color: #fff; letter-spacing: 0.4px;
  }
</style>
</head>
<body>
  <main class="letterhead">
    <div class="brand-name">North Peak Kitchenware</div>

    <section class="letter">
      <p class="recipient">Someone Somebody<br>72 Harbour Rd<br>Brisbane, Australia</p>
      <p class="greeting">Dear Someone Somebody,</p>
      <p class="body-text">Thank you for your recent inquiry about our commercial kitchen equipment. We are pleased to confirm that your order has been received and is now being prepared at our Anchorage warehouse. Our team will contact you shortly with delivery details, installation options and a full summary of the items you selected for your new restaurant.</p>
      <p class="body-text">Every product we supply is tested for durability and backed by our service guarantee. If you have questions about warranties, spare parts or training for your staff, please reach out to our support desk at any time during business hours.</p>
      <p class="body-text">We value the trust you have placed in us and look forward to supporting your kitchen for many years to come. Thank you again for choosing our company as your equipment partner.</p>
      <p class="sign-off">Your Sincerely,<br>Martin Keller.</p>
      <div class="signature-row">
        <div class="signature-mark" role="img" aria-label="Handwritten signature"></div>
        <div class="seal-badge"></div>
      </div>
    </section>

    <footer class="footer-band">
      <svg class="band-shape" viewBox="0 0 780 80" preserveAspectRatio="none" aria-hidden="true">
        <defs>
          <linearGradient id="bandBlue" x1="0" x2="1" y1="0" y2="0">
            <stop offset="0" stop-color="#1f4596"/>
            <stop offset="1" stop-color="#2f62b2"/>
          </linearGradient>
        </defs>
        <rect x="0" y="12" width="780" height="68" fill="url(#bandBlue)"/>
        <polygon points="476,12 494,12 532,80 514,80" fill="#ffffff"/>
        <polygon points="480,0 780,0 780,28 496,28" fill="#c63a4b"/>
      </svg>
      <ul class="contact-list">
        <li><svg class="contact-icon" viewBox="0 0 24 24" aria-hidden="true"><path d="M6.6 10.8a15 15 0 0 0 6.6 6.6l2.2-2.2c.3-.3.7-.4 1-.2 1.1.4 2.3.6 3.6.6.6 0 1 .4 1 1V20c0 .6-.4 1-1 1A17 17 0 0 1 3 4c0-.6.4-1 1-1h3.5c.6 0 1 .4 1 1 0 1.3.2 2.5.6 3.6.1.3 0 .7-.2 1z"/></svg>907.418.3952</li>
        <li><svg class="contact-icon" viewBox="0 0 24 24" aria-hidden="true"><path d="M6.6 10.8a15 15 0 0 0 6.6 6.6l2.2-2.2c.3-.3.7-.4 1-.2 1.1.4 2.3.6 3.6.6.6 0 1 .4 1 1V20c0 .6-.4 1-1 1A17 17 0 0 1 3 4c0-.6.4-1 1-1h3.5c.6 0 1 .4 1 1 0 1.3.2 2.5.6 3.6.1.3 0 .7-.2 1z"/></svg>855.392.6180 (Toll Free)</li>
        <li><svg class="contact-icon" viewBox="0 0 24 24" aria-hidden="true"><path d="M6 3h10v5H6zM4 9h16a2 2 0 0 1 2 2v7h-4v3H6v-3H2v-7a2 2 0 0 1 2-2zm4 7v3h8v-3z"/></svg>907.418.5263</li>
      </ul>
      <p class="address">4837 Birchwood Lane<br>Anchorage, AK 99517</p>
      <p class="website">www.northpeakkitchenware.com</p>
    </footer>
  </main>
</body>
</html>
```